Building Servicess

We need a new business card design for a company. We specialise in: Electrical/Site temporary electrics, Data/Network Installation, Passive Fire Protection

Industry/Entity Type

Construction

Contact Information for Business Card

Services provided as detailed on project description

Font styles to use
Serif

Colors
0054AA
0677BA
7BADD7
CADEEF
E8F1F8
00AB8E
00BBA5
67D7C9
C6EFE9
E9F9F6
EB3D1F
EC4F4E
F09395
F8D3D4
FCEDEE

Requirements
Must have
• Company logo-contact details-phone numbers

```html
<!DOCTYPE html>
<html lang="en">
<head>
<meta charset="utf-8">
<title>Norvale Build Services – Business Card</title>
<link href="https://fonts.googleapis.com/css2?family=Montserrat:wght@400;600;700&display=swap" rel="stylesheet">
<style>
  :root{
    --brand-blue:#1275BE;
    --brand-grey:#808285;
    --ink:#222222;
    --paper:#FFFFFF;
    --backdrop:#E9EEF3;
  }
  *{box-sizing:border-box;margin:0;padding:0}
  html,body{width:1200px;height:900px;overflow:hidden}
  body{background:var(--backdrop);font-family:"Montserrat",Arial,sans-serif;position:relative}
  .card{position:absolute;left:250px;width:700px;height:400px;overflow:hidden;box-shadow:0 6px 18px rgba(0,0,0,.18)}
  .card--front{top:30px;background:var(--brand-blue);color:var(--paper)}
  .card--back{top:470px;background:var(--paper)}

  .wordmark{position:absolute;font-weight:700;text-transform:uppercase;letter-spacing:1px;display:flex;align-items:center;gap:14px;white-space:nowrap}
  .wordmark__box{display:inline-block;flex:none;width:26px;height:26px}
  .card--front .wordmark{left:0;right:0;top:120px;justify-content:center;font-size:38px;color:var(--paper)}
  .card--front .wordmark__box{background:var(--paper)}
  .wordmark-rule{position:absolute;height:2px}
  .card--front .wordmark-rule{left:150px;width:400px;top:190px;background:var(--paper)}
  .services{position:absolute;left:0;right:0;top:290px;text-align:center;font-family:Arial,Helvetica,sans-serif;font-size:15px;line-height:1.45;letter-spacing:.5px;text-transform:uppercase}

  .card--back .wordmark{right:40px;top:84px;font-size:20px;gap:10px;letter-spacing:.5px;color:var(--brand-blue)}
  .card--back .wordmark__box{background:var(--brand-blue);width:18px;height:18px}
  .card--back .wordmark-rule{right:40px;width:300px;top:118px;background:var(--brand-grey)}
  .person{position:absolute;left:50px;top:60px}
  .person__name{font-size:24px;font-weight:700;color:var(--brand-blue);text-transform:uppercase;letter-spacing:.5px}
  .person__role{font-family:Arial,Helvetica,sans-serif;font-size:15px;color:var(--ink);text-transform:uppercase;letter-spacing:.5px}
  .contacts{position:absolute;left:50px;top:222px;list-style:none;font-family:Arial,Helvetica,sans-serif;font-size:17px;color:var(--ink)}
  .contacts li{display:flex;align-items:center;gap:10px;height:26px}
  .contacts .ico{width:20px;height:20px;background:var(--brand-blue);border-radius:3px;display:flex;align-items:center;justify-content:center}
  .contacts .ico svg{width:14px;height:14px}
  .contacts .mail{text-transform:uppercase}
  .swoosh{position:absolute;left:0;top:0;width:700px;height:400px}
  .website{position:absolute;right:40px;bottom:80px;color:var(--paper);font-family:Arial,Helvetica,sans-serif;font-size:15px;text-transform:uppercase;letter-spacing:.5px}
</style>
</head>
<body>

<section class="card card--front" aria-label="Card front">
  <div class="wordmark"><span class="wordmark__box"></span>Norvale Build Services</div>
  <div class="wordmark-rule"></div>
  <p class="services">Electrical/Site Temporary Electrics<br>Data/Network Installation | Passive Fire Protection</p>
</section>

<section class="card card--back" aria-label="Card back">
  <svg class="swoosh" viewBox="0 0 700 400" preserveAspectRatio="none" aria-hidden="true">
    <path d="M0 330 C200 330 330 320 460 230 C540 180 610 150 700 140 L700 400 L0 400 Z" fill="#808285"/>
    <path d="M0 350 C220 350 360 330 480 245 C560 190 620 165 700 155 L700 400 L0 400 Z" fill="#FFFFFF"/>
    <path d="M0 360 C230 360 380 335 500 250 C570 200 630 175 700 165 L700 400 L0 400 Z" fill="#1275BE"/>
  </svg>

  <div class="wordmark"><span class="wordmark__box"></span>Norvale Build Services</div>
  <div class="wordmark-rule"></div>

  <div class="person">
    <p class="person__name">Tomas Brennan</p>
    <p class="person__role">Managing Director</p>
  </div>

  <ul class="contacts">
    <li><span class="ico"><svg viewBox="0 0 24 24"><path fill="#fff" d="M6.6 10.8a15 15 0 0 0 6.6 6.6l2.2-2.2a1 1 0 0 1 1-.25 11 11 0 0 0 3.6.6 1 1 0 0 1 1 1V20a1 1 0 0 1-1 1A17 17 0 0 1 3 4a1 1 0 0 1 1-1h3.5a1 1 0 0 1 1 1 11 11 0 0 0 .6 3.6 1 1 0 0 1-.25 1z"/></svg></span>020 7946 0183</li>
    <li><span class="ico"><svg viewBox="0 0 24 24"><rect x="6" y="2" width="12" height="20" rx="2" fill="#fff"/><rect x="8" y="5" width="8" height="12" fill="#1275BE"/></svg></span>07700900412</li>
    <li><span class="ico"><svg viewBox="0 0 24 24"><rect x="2" y="5" width="20" height="14" fill="#fff"/><path d="M2 5l10 8 10-8" stroke="#1275BE" stroke-width="2" fill="none"/></svg></span><span class="mail">info@norvalebuild.com</span></li>
  </ul>

  <p class="website">www.norvalebuild.com</p>
</section>

</body>
</html>
```